Industrial Automation company requires a business card design

Valtrin Automation provides design & build of Automated Equipment for manufacturing industry.
www.valtrinautomation.example
The equipment we design is used for manufacturing in sectors such as medical device, pharmaceutical, aerospace and electronics.
We require a new business card design which incorporates our (New) logo and the key message words:
Automated Equipment:
Design, Build, Control, Test, Support

```html
<!DOCTYPE html>
<html lang="en">
<head>
<meta charset="utf-8">
<title>Valtrin Automation – Business Card</title>
<link href="https://fonts.googleapis.com/css2?family=Open+Sans:wght@400;600;700&display=swap" rel="stylesheet">
<style>
  :root {
    --backdrop: #e4ddd3;
    --card-white: #ffffff;
    --card-black: #121212;
    --brand-green: #168a43;
    --band-green: #127a3b;
    --band-dark: #231f20;
    --ink: #1e1e1e;
    --ink-soft: #3a3a3a;
  }
  * { box-sizing: border-box; margin: 0; padding: 0; }
  html, body {
    width: 1200px; height: 900px; overflow: hidden;
    background: var(--backdrop);
    font-family: "Open Sans", Arial, sans-serif;
  }
  .stage {
    position: relative; width: 1200px; height: 900px;
    display: flex; flex-direction: column; align-items: center; justify-content: center; gap: 40px;
  }
  .card {
    position: relative; width: 640px; height: 366px; overflow: hidden;
    box-shadow: 0 10px 24px rgba(0,0,0,.18);
  }

  /* Back of card */
  .card--back { background: var(--card-black); color: #fff; }
  .back-brand {
    position: absolute; left: 0; right: 0; top: 104px; text-align: center;
    font-weight: 700; line-height: 1;
  }
  .back-brand__name { display: block; font-size: 64px; letter-spacing: 4px; }
  .back-brand__sub { display: block; font-size: 24px; letter-spacing: 18px; margin-top: 6px; padding-left: 18px; }
  .services {
    position: absolute; left: 0; right: 0; top: 250px;
    display: flex; justify-content: center; gap: 16px; list-style: none;
    font-size: 19px; font-weight: 400;
  }
  .services li { display: flex; align-items: center; gap: 5px; }
  .services svg { width: 8px; height: 9px; fill: #fff; }

  /* Front of card */
  .card--front { background: var(--card-white); color: var(--ink); }
  .front-shapes { position: absolute; inset: 0; }
  .holder { position: absolute; left: 78px; top: 24px; }
  .holder__name { font-size: 20px; font-weight: 700; color: var(--brand-green); }
  .holder__title { font-size: 14px; color: var(--ink-soft); margin-top: -2px; }
  .address { position: absolute; left: 36px; top: 118px; font-size: 15px; line-height: 1.3; }
  .contacts { position: absolute; left: 36px; top: 168px; list-style: none; font-size: 15px; line-height: 1.3; }
  .contacts li { display: flex; align-items: center; gap: 9px; }
  .contacts svg { width: 11px; height: 11px; fill: var(--ink); flex: none; }
  .front-brand {
    position: absolute; left: 330px; top: 124px;
    display: flex; align-items: center; gap: 14px;
    color: var(--brand-green); font-weight: 700; line-height: 1;
  }
  .front-brand__dot { width: 44px; height: 44px; border-radius: 50%; background: var(--brand-green); }
  .front-brand__name { display: block; font-size: 44px; letter-spacing: 3px; }
  .front-brand__sub { display: block; font-size: 17px; letter-spacing: 11px; margin-top: 4px; }
</style>
</head>
<body>
<main class="stage">

  <section class="card card--back" aria-label="Business card back">
    <h1 class="back-brand">
      <span class="back-brand__name">VALTRIN</span>
      <span class="back-brand__sub">AUTOMATION</span>
    </h1>
    <ul class="services">
      <li><svg viewBox="0 0 8 9"><path d="M0 0L8 4.5L0 9Z"/></svg>Design</li>
      <li><svg viewBox="0 0 8 9"><path d="M0 0L8 4.5L0 9Z"/></svg>Build</li>
      <li><svg viewBox="0 0 8 9"><path d="M0 0L8 4.5L0 9Z"/></svg>Control</li>
      <li><svg viewBox="0 0 8 9"><path d="M0 0L8 4.5L0 9Z"/></svg>Test</li>
      <li><svg viewBox="0 0 8 9"><path d="M0 0L8 4.5L0 9Z"/></svg>Support</li>
    </ul>
  </section>

  <section class="card card--front" aria-label="Business card front">
    <svg class="front-shapes" viewBox="0 0 640 366" aria-hidden="true">
      <path d="M18 24H70L18 58Z" fill="var(--band-green)"/>
      <path d="M72 24V72H26Z" fill="var(--band-dark)"/>
      <path d="M0 262H300L282 290H0Z" fill="var(--band-green)"/>
      <path d="M300 290H640V366H260Z" fill="var(--band-dark)"/>
      <path d="M286 290H300L260 366H246Z" fill="var(--card-white)"/>
    </svg>

    <div class="holder">
      <p class="holder__name">Marcus Ellery</p>
      <p class="holder__title">Managing Director</p>
    </div>

    <address class="address" style="font-style:normal">
      12345, Address Goes Here<br>
      Country Name, 123456.
    </address>

    <ul class="contacts">
      <li><svg viewBox="0 0 12 12"><path d="M2 0h3l1 3-2 1a7 7 0 0 0 4 4l1-2 3 1v3c0 1-1 2-2 2A10 10 0 0 1 0 2c0-1 1-2 2-2z"/></svg>044-555 010 789</li>
      <li><svg viewBox="0 0 12 12"><path d="M3 0h6v4H3zM1 5h10v5H1zM3 8h6v4H3z"/></svg>044-555 010 789</li>
      <li><svg viewBox="0 0 12 12"><path d="M0 2h12v8H0zM1 3l5 4 5-4z" fill-rule="evenodd"/></svg>info@valtrinmail.example</li>
      <li><svg viewBox="0 0 12 12"><circle cx="6" cy="6" r="6"/></svg>www.valtrinautomation.example</li>
    </ul>

    <div class="front-brand">
      <span class="front-brand__dot"></span>
      <p>
        <span class="front-brand__name">VALTRIN</span>
        <span class="front-brand__sub">AUTOMATION</span>
      </p>
    </div>
  </section>

</main>
</body>
</html>
```